Ledgerwise Capital Business Cards

We are looking to revamp the current business cards each of our locations uses. We are a lending company that specializes in personal loans, title loans, and tax services. We have locations in New Mexico, Texas, and Oklahoma.

We would like a cleaner, sleeker look while still highlighting what we offer. Title Loans, Personal Loans & Tax Services. We also want to include our referral fee somewhere on the card. We would like to see an English option as well as a Spanish option for the cards.

PLEASE NOTE: Some business cards do not include the employee's name but just the store's location, while others will include both.

These are double-sided business cards, and we would like to see proof if possible. I have included proofs of our current business cards for you to review below, as well as our company logo. Feel free to get creative with the logo, etc! Colors should match the logo; however, you do not need to use all of our logo colors if you don't want to.

```html
<!DOCTYPE html>
<html lang="en">
<head>
<meta charset="utf-8">
<title>Ledgerwise Capital Business Cards</title>
<link rel="stylesheet" href="https://fonts.googleapis.com/css2?family=Montserrat:wght@400;500;600;700;800&display=swap">
<style>
  :root {
    --green: #0e4f2c;
    --red: #c41f26;
    --red-dark: #7d161b;
    --white: #ffffff;
    --page: #ececec;
    --edge: #d2d2d2;
  }
  * { margin: 0; padding: 0; box-sizing: border-box; }
  html, body { width: 1200px; height: 1000px; overflow: hidden; background: var(--page); }
  body { font-family: "Montserrat", Arial, sans-serif; position: relative; }

  .card { position: absolute; left: 312px; width: 554px; height: 318px; background: var(--white); overflow: hidden; outline: 1px solid var(--edge); }
  .card--front { top: 139px; }
  .card--back { top: 524px; }

  /* Front */
  .brand-panel { position: absolute; left: 0; top: 0; width: 196px; height: 100%; background: var(--green); }
  .brand-panel__name {
    position: absolute; left: 98px; top: 159px;
    transform: translate(-50%, -50%) rotate(-90deg);
    white-space: nowrap; color: var(--white); font-weight: 600; font-size: 26px; letter-spacing: 0.5px;
  }
  .front__web { position: absolute; left: 196px; right: 0; top: 17px; text-align: center; color: var(--red); font-weight: 700; font-size: 16px; white-space: nowrap; }
  .ribbon { position: absolute; left: 162px; top: 55px; width: 392px; height: 114px; background: var(--red); }
  .ribbon__fold { position: absolute; left: 162px; top: 169px; width: 34px; height: 24px; }
  .ribbon__text { position: absolute; left: 233px; top: 66px; color: var(--white); font-weight: 800; font-size: 43px; line-height: 44px; letter-spacing: 0.5px; white-space: nowrap; }
  .offer__lead { position: absolute; left: 233px; top: 190px; color: var(--green); font-weight: 800; font-size: 24px; }
  .offer__amount { position: absolute; left: 231px; top: 220px; color: var(--green); font-weight: 800; font-size: 78px; line-height: 84px; }

  /* Back */
  .services { position: absolute; left: 33px; top: 29px; list-style: none; }
  .services__item { display: flex; align-items: center; height: 33px; color: var(--red); font-weight: 700; font-size: 21px; white-space: nowrap; }
  .services__item svg { width: 22px; height: 22px; margin-right: 14px; }
  .back__brand { position: absolute; left: 276px; width: 264px; top: 76px; text-align: center; color: var(--green); font-weight: 600; font-size: 23px; white-space: nowrap; }
  .contact-band { position: absolute; left: 0; top: 150px; width: 100%; height: 136px; background: var(--green); color: var(--white); }
  .person__name { position: absolute; left: 33px; top: 44px; font-weight: 700; font-size: 23px; }
  .person__role { position: absolute; left: 33px; top: 72px; font-weight: 500; font-size: 15px; }
  .contacts { position: absolute; left: 274px; top: 27px; list-style: none; }
  .contacts__item { display: flex; align-items: center; height: 28px; font-size: 14px; font-weight: 500; white-space: nowrap; }
  .contacts__item svg { width: 22px; height: 22px; margin-right: 28px; flex: none; }
  .address { position: absolute; left: 0; right: 0; top: 294px; text-align: center; color: var(--red); font-weight: 500; font-size: 15px; }
</style>
</head>
<body>
  <section class="card card--front" aria-label="Business card front">
    <div class="brand-panel"><span class="brand-panel__name">Ledgerwise Capital</span></div>
    <p class="front__web">www.ledgerwisecapital.com</p>
    <div class="ribbon"></div>
    <svg class="ribbon__fold" viewBox="0 0 34 24" aria-hidden="true"><polygon points="0,0 34,0 34,24" fill="var(--red-dark)"/></svg>
    <h2 class="ribbon__text">REFER<br>A FRIENDS</h2>
    <p class="offer__lead">GET UP TO</p>
    <p class="offer__amount">$100</p>
  </section>

  <section class="card card--back" aria-label="Business card back">
    <ul class="services">
      <li class="services__item"><svg viewBox="0 0 24 24" aria-hidden="true"><circle cx="12" cy="12" r="10" fill="none" stroke="var(--green)" stroke-width="2.4"/><path d="M7 12.5l3.3 3.3L17 9" fill="none" stroke="var(--green)" stroke-width="2.6" stroke-linecap="round" stroke-linejoin="round"/></svg>Title Loans</li>
      <li class="services__item"><svg viewBox="0 0 24 24" aria-hidden="true"><circle cx="12" cy="12" r="10" fill="none" stroke="var(--green)" stroke-width="2.4"/><path d="M7 12.5l3.3 3.3L17 9" fill="none" stroke="var(--green)" stroke-width="2.6" stroke-linecap="round" stroke-linejoin="round"/></svg>Personal Loans</li>
      <li class="services__item"><svg viewBox="0 0 24 24" aria-hidden="true"><circle cx="12" cy="12" r="10" fill="none" stroke="var(--green)" stroke-width="2.4"/><path d="M7 12.5l3.3 3.3L17 9" fill="none" stroke="var(--green)" stroke-width="2.6" stroke-linecap="round" stroke-linejoin="round"/></svg>Tax Services</li>
    </ul>
    <p class="back__brand">Ledgerwise Capital</p>

    <div class="contact-band">
      <p class="person__name">Jane Doe</p>
      <p class="person__role">Branch Manager</p>
      <ul class="contacts">
        <li class="contacts__item"><svg viewBox="0 0 24 24" aria-hidden="true"><path d="M15 6c-4 0-7 3-8 8l-1 4 2 1c1-5 3-8 7-9z" fill="var(--white)"/></svg>(505) 555-1212</li>
        <li class="contacts__item"><svg viewBox="0 0 24 24" aria-hidden="true"><rect x="2" y="5" width="20" height="14" fill="var(--white)"/><path d="M2 5l10 8 10-8" fill="none" stroke="var(--green)" stroke-width="1.6"/></svg>abcde@ledgerwisecapital.com</li>
        <li class="contacts__item"><svg viewBox="0 0 24 24" aria-hidden="true"><g fill="none" stroke="var(--white)" stroke-width="1.5"><circle cx="12" cy="12" r="9.5"/><ellipse cx="12" cy="12" rx="4.2" ry="9.5"/><path d="M2.5 12h19M4 7h16M4 17h16M12 2.5v19"/></g></svg>www.ledgerwisecapital.com</li>
      </ul>
    </div>
    <p class="address">123 Elm Street, Suite B, Anytown, Texas 55555</p>
  </section>
</body>
</html>
```